Non-Fiction Book Cover Series Concepts

I need front cover concepts for a non-fiction business book series. Just concepts at this stage to show to backers (full cover designs later).

The books are for leaders and business owners. A mature, sophisticated market, AND, bold and innovative.

The series needs to be extensible - the concepts need to be able to work across at least 40 books. I am happy with a colour theme, or contrasts, or icon theme, there is no limitation to the imagination.

The books need to look like they belong to a series and to also stand alone.

I prefer simple and bold.

Imagine the Heron trade series (https://www.heronbooks.example/series/tws/heron-trade-wisdom-series.html) - but I hate these designs (the colours don't work for me).

The imprint is MindfulVantagePress.example - the logo mark for the imprint is attached.

The books will be printed and ebooks - the printed version will be 5 inches by 8 inches form factor. They will be printed with a matt cover.

IF YOU WANT A BOOK TITLE TO TRY, use this:

Steady Momentum: Apply the R.A.V. Model to Inspire, Unlock and Sustain Talent

Thank you for your interest!

Target Market(s)

Business owners, leaders, entrepreneurs

Industry/Entity Type

Leadership

Font styles to use
Serif
Sans Serif

Requirements
Must have
• Extensible - the concept can work for many books and ALL books look part of the series
Nice to have
• I prefer simple, icons rather than photos
Should not have
• No photographic designs - icon, drawing

```html
<!DOCTYPE html>
<html lang="en">
<head>
<meta charset="utf-8">
<title>Heron Trade Series – Cover Concepts</title>
<link rel="stylesheet" href="https://fonts.googleapis.com/css2?family=Archivo:wght@500;600;700&display=swap">
<style>
  :root {
    --board-grey: #cbcbcb;
    --board-pink: #f6c6c6;
    --violet-deep: #32246a;
    --violet-ink: #6b4ee6;
    --violet-muted: #4b4470;
    --violet-slash: #4a4470;
    --night: #0d1216;
    --night-soft: #161b1f;
    --white: #ffffff;
  }
  * { margin: 0; padding: 0; box-sizing: border-box; }
  html, body { width: 1200px; height: 950px; overflow: hidden; }
  body { font-family: "Archivo", Arial, sans-serif; position: relative; background: var(--board-pink); }
  .board-top { position: absolute; left: 0; top: 0; width: 1200px; height: 534px; background: var(--board-grey); }
  .board-bottom { position: absolute; left: 0; top: 534px; width: 1200px; height: 416px;
    background: linear-gradient(180deg, #f1bcbc 0%, #f9d0d0 100%); }
  .cover { position: absolute; display: block; }
  .cover--row { top: 96px; width: 252px; height: 360px; }
  .cover--violet { left: 70px; }
  .cover--night { left: 345px; }
  .cover--lined { left: 617px; }
  .cover--bold { left: 881px; }
  .cover--feature { top: 592px; width: 222px; height: 305px; }
  .cover--feature-bold { left: 193px; }
  .cover--feature-lined { left: 772px; }
  .imprint { font-weight: 600; font-size: 9px; }
  .title-small { font-weight: 500; font-size: 23px; }
  .title-large { font-weight: 700; font-size: 38px; }
  .quote-text { font-size: 5.6px; font-weight: 500; }
  .defs { position: absolute; width: 0; height: 0; }
</style>
</head>
<body>
  <div class="board-top"></div>
  <div class="board-bottom"></div>

  <svg class="defs" aria-hidden="true">
    <defs>
      <linearGradient id="lined-ground" x1="0" y1="0" x2="1" y2="1">
        <stop offset="0" stop-color="#1b2024"/>
        <stop offset="0.6" stop-color="#121619"/>
        <stop offset="1" stop-color="#0c1013"/>
      </linearGradient>

      <symbol id="cover-violet" viewBox="0 0 351 501">
        <rect width="351" height="501" fill="var(--violet-deep)"/>
        <rect x="324" width="27" height="501" fill="var(--night)"/>
        <text class="imprint" x="16" y="45" fill="var(--violet-ink)">MindfulVantagePress</text>
        <rect x="16" y="51" width="234" height="3" fill="var(--violet-muted)"/>
        <circle cx="286" cy="52" r="7" fill="var(--violet-ink)"/>
        <line x1="176" y1="212" x2="240" y2="117" stroke="var(--violet-slash)" stroke-width="14"/>
        <line x1="218" y1="214" x2="284" y2="119" stroke="var(--violet-slash)" stroke-width="14"/>
        <polygon points="0,272 28,244 80,300 0,388" fill="var(--violet-muted)"/>
        <circle cx="142" cy="318" r="95" fill="#3a2e6e"/>
        <circle cx="132" cy="310" r="84" fill="var(--violet-muted)"/>
        <text class="title-small" x="62" y="299" fill="var(--violet-ink)">YOUR BOOK</text>
        <text class="title-large" x="62" y="347" fill="var(--violet-ink)">TITLE</text>
      </symbol>

      <symbol id="cover-night" viewBox="0 0 351 501">
        <rect width="351" height="501" fill="var(--night)"/>
        <rect x="324" width="27" height="501" fill="var(--violet-deep)"/>
        <text class="imprint" x="16" y="45" fill="var(--violet-ink)">MindfulVantagePress</text>
        <rect x="16" y="51" width="234" height="3" fill="var(--violet-muted)"/>
        <circle cx="286" cy="52" r="7" fill="var(--violet-ink)"/>
        <line x1="176" y1="194" x2="240" y2="98" stroke="var(--violet-slash)" stroke-width="14"/>
        <line x1="218" y1="196" x2="284" y2="100" stroke="var(--violet-slash)" stroke-width="14"/>
        <polygon points="0,272 28,244 80,300 0,388" fill="var(--violet-muted)"/>
        <circle cx="137" cy="314" r="84" fill="#000000"/>
        <circle cx="132" cy="310" r="84" fill="var(--violet-muted)"/>
        <text class="title-small" x="62" y="299" fill="var(--violet-ink)">YOUR BOOK</text>
        <text class="title-large" x="62" y="347" fill="var(--violet-ink)">TITLE</text>
        <text x="76" y="448" font-size="17" font-weight="700" fill="var(--white)">&#8220;</text>
        <text class="quote-text" x="100" y="445" fill="var(--white)">Lorem ipsum dolor sit amet, consectetuer</text>
        <text class="quote-text" x="100" y="453" fill="var(--white)">adipiscing elit, sed diam nonummy nibh euismod</text>
        <text x="251" y="458" font-size="17" font-weight="700" fill="var(--white)">&#8221;</text>
      </symbol>

      <symbol id="cover-lined" viewBox="0 0 351 501">
        <rect width="351" height="501" fill="url(#lined-ground)" role="img" aria-label="Dark ground with fine diagonal line texture"/>
        <rect x="324" width="27" height="501" fill="var(--night-soft)"/>
        <text class="imprint" x="16" y="45" fill="var(--violet-ink)">MindfulVantagePress</text>
        <rect x="16" y="51" width="234" height="3" fill="var(--violet-muted)"/>
        <circle cx="286" cy="52" r="7" fill="var(--violet-ink)"/>
        <line x1="176" y1="194" x2="240" y2="98" stroke="var(--violet-slash)" stroke-width="14"/>
        <line x1="218" y1="196" x2="284" y2="100" stroke="var(--violet-slash)" stroke-width="14"/>
        <polygon points="0,272 28,244 80,300 0,388" fill="var(--violet-muted)"/>
        <circle cx="137" cy="314" r="84" fill="#000000"/>
        <circle cx="132" cy="310" r="84" fill="var(--violet-muted)"/>
        <text class="title-small" x="62" y="299" fill="var(--white)">YOUR BOOK</text>
        <text class="title-large" x="62" y="347" fill="var(--white)">TITLE</text>
      </symbol>

      <symbol id="cover-bold" viewBox="0 0 351 501">
        <rect width="351" height="501" fill="var(--violet-deep)"/>
        <rect x="324" width="27" height="501" fill="var(--violet-muted)"/>
        <text class="imprint" x="16" y="46" fill="var(--white)">MindfulVantagePress</text>
        <rect x="16" y="51" width="234" height="3" fill="var(--white)"/>
        <circle cx="286" cy="52" r="7" fill="var(--violet-ink)"/>
        <polygon points="0,258 18,240 60,300 0,368" fill="var(--violet-muted)"/>
        <line x1="170" y1="372" x2="300" y2="226" stroke="var(--violet-muted)" stroke-width="30"/>
        <line x1="250" y1="364" x2="324" y2="282" stroke="var(--violet-muted)" stroke-width="24"/>
        <circle cx="132" cy="308" r="86" fill="var(--violet-muted)"/>
        <text class="title-small" x="61" y="296" fill="var(--white)">YOUR BOOK</text>
        <text class="title-large" x="61" y="343" fill="var(--white)">TITLE</text>
      </symbol>
    </defs>
  </svg>

  <svg class="cover cover--row cover--violet" role="img" aria-label="Cover concept, violet"><use href="#cover-violet"/></svg>
  <svg class="cover cover--row cover--night" role="img" aria-label="Cover concept, night with quote"><use href="#cover-night"/></svg>
  <svg class="cover cover--row cover--lined" role="img" aria-label="Cover concept, lined night"><use href="#cover-lined"/></svg>
  <svg class="cover cover--row cover--bold" role="img" aria-label="Cover concept, bold violet"><use href="#cover-bold"/></svg>

  <svg class="cover cover--feature cover--feature-bold" role="img" aria-label="Featured cover, bold violet"><use href="#cover-bold"/></svg>
  <svg class="cover cover--feature cover--feature-lined" role="img" aria-label="Featured cover, lined night"><use href="#cover-lined"/></svg>
</body>
</html>
```